Looking for a hot sauce label designed
Name: Copper Lantern Hot sauce
Graphic: dragon in pictures supplied and the flame bigger going out in front of the dragon or happy for you to design a dragon in a similar style
Text font: using the text supplied for the name of the product only
Colour: Black graphic and text on light brown paper
Style: sketch dragon and text - simple minimalistic design
Label size: 7cm height x 17cm width

Target Market(s)

To sell in bars and supermarkets

Font styles to use
Script

Colors

Designer to choose only greyscale colors for use in the design.

Requirements
Must have
• Name of product: Copper Lantern Hot Sauce
Batch No:
Copper Lantern Sauce Co., 14 Tallow Lane, Geelong VIC 3220
Best before date:
Nutrition Information Panel
Ingredients
Shake well before use
Keep refrigerated after opening
Australian made using 100% local ingredients
175ml
Room for a barcode
Nice to have
• Any changes you think will improve label design

```html
<!DOCTYPE html>
<html lang="en">
<head>
<meta charset="utf-8">
<title>Copper Lantern Hot Sauce – Bottle Label</title>
<link href="https://fonts.googleapis.com/css2?family=Caveat:wght@500&family=Patrick+Hand&family=Sarabun:wght@500&family=Arimo:wght@400;700&family=PT+Sans&display=swap" rel="stylesheet">
<style>
  :root {
    --backdrop: #777777;
    --paper: #dcc8a6;
    --ink: #111111;
    --ink-soft: #3a3a3a;
    --grey-mid: #6e6e6e;
    --grey-light: #b8b8b8;
  }
  * { margin: 0; padding: 0; box-sizing: border-box; }
  html, body { width: 1200px; height: 1200px; overflow: hidden; background: var(--backdrop); }
  .label {
    position: absolute; left: 70px; top: 352px; width: 1063px; height: 496px;
    background: var(--paper); color: var(--ink);
  }
  .nutrition {
    position: absolute; left: 31px; top: 49px; width: 243px; height: 256px;
    border: 2px solid var(--ink);
    font-family: "Sarabun", sans-serif; font-weight: 500; font-size: 13.5px;
  }
  .nutrition-title { position: absolute; left: 0; right: 0; top: 4px; text-align: center; }
  .nutrition-row { position: absolute; left: 9px; white-space: nowrap; }
  .col-a { position: absolute; left: 95px; white-space: nowrap; }
  .col-b { position: absolute; left: 168px; white-space: nowrap; }
  .caution {
    position: absolute; left: 31px; top: 305px; width: 231px; height: 159px;
    border: 2px solid var(--ink); border-top: none;
  }
  .caution-title {
    position: absolute; left: 11px; top: 7px;
    font-family: "Arimo", sans-serif; font-weight: 700; font-size: 14px; letter-spacing: -0.4px;
  }
  .caution-title u { text-decoration: underline; }
  .caution-item {
    position: absolute; left: 9px; font-family: "Arimo", sans-serif; font-weight: 700;
    font-size: 14px; letter-spacing: -0.5px; white-space: nowrap;
  }
  .caution-item span { display: inline-block; width: 17px; }
  .ingredients {
    position: absolute; left: 9px; top: 72px; width: 212px;
    font-family: "PT Sans", sans-serif; font-size: 12.5px; line-height: 17px; letter-spacing: -0.3px;
  }
  .ingredients strong { font-family: "Arimo", sans-serif; font-size: 14px; letter-spacing: -0.6px; }
  .product-name {
    position: absolute; left: 300px; width: 560px; top: 20px; text-align: center;
    font-family: "Caveat", cursive; font-weight: 500; font-size: 92px; line-height: 1;
    color: var(--ink);
  }
  .product-type {
    position: absolute; left: 300px; width: 560px; top: 124px; text-align: center;
    font-family: "Patrick Hand", cursive; font-weight: 400; font-size: 58px; line-height: 1;
    letter-spacing: 4px; color: var(--ink-soft);
  }
  .product-type .sauce { margin-left: 28px; }
  .mascot { position: absolute; left: 465px; top: 218px; width: 345px; height: 243px; }
  .usage {
    position: absolute; left: 290px; top: 232px; width: 165px;
    font-family: "Arimo", sans-serif; font-size: 11px; line-height: 15px; letter-spacing: -0.2px;
  }
  .usage .strong { font-weight: 700; }
  .usage .best-before { margin-top: 6px; font-weight: 700; }
  .usage .best-before span { display: inline-block; width: 70px; border-bottom: 1px solid var(--ink); }
  .usage .maker { margin-top: 6px; }
  .barcode-space {
    position: absolute; left: 290px; top: 345px; width: 150px; height: 82px;
    border: 1.5px dashed var(--grey-mid);
  }
  .volume {
    position: absolute; left: 348px; top: 442px;
    font-family: "Arimo", sans-serif; font-weight: 700; font-size: 13.5px; letter-spacing: -0.4px;
  }
  .origin { position: absolute; left: 948px; top: 45px; width: 40px; height: 222px; }
  .origin p {
    position: absolute; left: 50%; top: 50%; width: 222px;
    transform: translate(-50%, -50%) rotate(-90deg); text-align: center;
    font-family: "Arimo", sans-serif; font-weight: 700; font-size: 15px; line-height: 19px; white-space: nowrap;
  }
  .batch {
    position: absolute; left: 947px; top: 280px; width: 42px; height: 186px;
    border: 2.5px solid var(--ink);
  }
  .batch p {
    position: absolute; left: 50%; top: 50%; width: 176px;
    transform: translate(-50%, -50%) rotate(-90deg);
    font-family: "Arimo", sans-serif; font-weight: 700; font-size: 15px; white-space: nowrap; padding-left: 6px;
    color: var(--ink);
  }
  .batch .blank { display: inline-block; width: 80px; margin-left: 6px; border-bottom: 1.5px solid var(--ink); }
</style>
</head>
<body>
<div class="label">
  <section class="nutrition">
    <div class="nutrition-title">NUTRITION INFORMATION</div>
    <div class="nutrition-row" style="top:28px">Servings per package:<span class="col-b" style="left:148px">17.00</span></div>
    <div class="nutrition-row" style="top:50px">Serving size:<span class="col-b" style="left:148px">170.00m</span></div>
    <div class="nutrition-row" style="top:74px;width:230px;height:40px">
      <span class="col-a" style="line-height:17px">Ave. per<br>serve</span>
      <span class="col-b" style="line-height:17px">Ave. per<br>100ml</span>
    </div>
    <div class="nutrition-row" style="top:117px">Energy<span class="col-a">257g</span><span class="col-b">151KJ</span></div>
    <div class="nutrition-row" style="top:137px">Protein<span class="col-a">1,5g</span><span class="col-b">0,9g</span></div>
    <div class="nutrition-row" style="top:157px">Fat, Total<span class="col-a">3.2g</span><span class="col-b">1,9g</span></div>
    <div class="nutrition-row" style="top:177px">&nbsp;- saturated<span class="col-a">0,5g</span><span class="col-b">0,3g</span></div>
    <div class="nutrition-row" style="top:196px">Carbohydrate<span class="col-a">4,3g</span><span class="col-b">2,5g</span></div>
    <div class="nutrition-row" style="top:215px">&nbsp;- sugars<span class="col-a">3,7g</span><span class="col-b">2,2g</span></div>
    <div class="nutrition-row" style="top:234px">Sodium<span class="col-a">262g</span><span class="col-b">154mg</span></div>
  </section>

  <section class="caution">
    <div class="caution-title"><u>CAUTION</u>:</div>
    <div class="caution-item" style="top:26px"><span>-</span>Keep out of reach of children</div>
    <div class="caution-item" style="top:42px"><span>-</span>Keep away and out of eyes</div>
    <p class="ingredients"><strong>INGREDIENTS:</strong> Carrots, onion, Habanero, water, lime juice, garlic, white vinegar, vegetable oil, ginger, cilantro, salt, pepper.</p>
  </section>

  <h1 class="product-name">Copper Lantern</h1>
  <h2 class="product-type"><span class="hot">Hot</span><span class="sauce">Sauce</span></h2>

  <section class="usage">
    <p class="strong">Shake well before use</p>
    <p class="strong">Keep refrigerated after opening</p>
    <p class="best-before">Best before: <span></span></p>
    <p class="maker">Copper Lantern Sauce Co.<br>14 Tallow Lane, Geelong VIC 3220</p>
  </section>
  <div class="barcode-space" aria-label="Space reserved for barcode"></div>

  <svg class="mascot" role="img" aria-label="Sketch illustration of a chubby dragon sitting and breathing a large flame" viewBox="0 0 345 243">
    <defs>
      <radialGradient id="mascot-fill" cx="55%" cy="55%" r="60%">
        <stop offset="0" stop-color="#9a9a9a"/>
        <stop offset="0.5" stop-color="#6e6e6e"/>
        <stop offset="1" stop-color="#6e6e6e" stop-opacity="0.12"/>
      </radialGradient>
    </defs>
    <rect width="345" height="243" rx="60" fill="url(#mascot-fill)"/>
  </svg>

  <div class="volume">175ml</div>

  <div class="origin"><p>MADE USING 100% FRESH<br>AUSTRALIAN PRODUCE</p></div>
  <div class="batch"><p>Batch No<span class="blank"></span></p></div>
</div>
</body>
</html>
```